Design some Business Cards

Looking for a very creative and unique design for a business card for a marketing firm. Needs to include the following:

Logo
URL: http://www.TheMarvilleGroup.example
Businesss Phone: 555-418-7093

Then it will need to be customized with individual contact info:
Name
Mobile #
E-mail

Do not include address

Logo attached

```html
<!DOCTYPE html>
<html lang="en">
<head>
<meta charset="utf-8">
<title>The Marville Group – Business Cards</title>
<link href="https://fonts.googleapis.com/css2?family=Open+Sans:wght@400;600;700&display=swap" rel="stylesheet">
<style>
  :root {
    --page-bg: #e4e6e8;
    --card-blue: #1f5f8c;
    --card-blue-light: #2f74a6;
    --card-blue-dark: #184d73;
    --card-white: #f7f7f7;
    --arc-gray: #6b6e72;
    --ink-white: #ffffff;
    --ink-soft: #d9e6f0;
    --logo-ink: #1f5f8c;
  }
  * { box-sizing: border-box; margin: 0; padding: 0; }
  html, body { width: 1200px; height: 799px; overflow: hidden; }
  body {
    background: var(--page-bg);
    font-family: "Open Sans", Arial, sans-serif;
    position: relative;
  }
  .card {
    position: absolute;
    width: 520px;
    height: 298px;
    top: 250px;
    border-radius: 3px;
    overflow: hidden;
    box-shadow: 0 12px 28px rgba(0,0,0,0.18);
  }
  .card--back {
    left: 45px;
    background: linear-gradient(135deg, var(--card-blue-light), var(--card-blue) 55%, var(--card-blue-dark));
  }
  .card--front {
    left: 635px;
    background: linear-gradient(135deg, var(--card-blue-light), var(--card-blue) 60%, var(--card-blue-dark));
  }

  /* Wordmark */
  .wordmark { position: absolute; display: flex; align-items: center; gap: 12px; }
  .wordmark__dot {
    width: 46px; height: 46px; border-radius: 50%;
    border: 3px solid currentColor;
  }
  .wordmark__name {
    font-weight: 700; font-size: 17px; line-height: 1.05;
    text-transform: uppercase; letter-spacing: 0.5px;
  }

  /* Back card */
  .card--back .wordmark { left: 50px; top: 118px; color: var(--ink-white); }
  .card--back .divider {
    position: absolute; left: 270px; top: 90px; width: 2px; height: 118px;
    background: rgba(255,255,255,0.55);
  }
  .services {
    position: absolute; left: 290px; top: 94px; list-style: none;
    color: var(--ink-white); font-size: 12.5px; line-height: 18px;
  }

  /* Front card */
  .front-curve { position: absolute; inset: 0; }
  .card--front .wordmark { right: 30px; top: 62px; color: var(--logo-ink); }
  .card--front .wordmark__name { font-size: 16px; }
  .identity { position: absolute; left: 30px; top: 112px; color: var(--ink-white); }
  .identity__name { font-size: 28px; font-weight: 400; line-height: 1.1; }
  .identity__title { font-size: 13px; color: var(--ink-soft); margin-top: 2px; }
  .contacts { position: absolute; left: 30px; top: 192px; list-style: none; color: var(--ink-white); font-size: 14px; }
  .contacts li { display: flex; align-items: center; gap: 12px; height: 28px; }
  .contacts svg { width: 20px; height: 20px; flex: none; }
</style>
</head>
<body>

<section class="card card--back" aria-label="Business card, back">
  <div class="wordmark">
    <span class="wordmark__dot"></span>
    <span class="wordmark__name">The Marville<br>Group</span>
  </div>
  <span class="divider"></span>
  <ul class="services">
    <li>Event &amp; Social Marketing</li>
    <li>Website Design &amp; Development</li>
    <li>Social Media Strategy</li>
    <li>Search Engine Optimization</li>
    <li>Email Marketing</li>
    <li>Content Creation</li>
  </ul>
</section>

<section class="card card--front" aria-label="Business card, front">
  <svg class="front-curve" viewBox="0 0 520 298" preserveAspectRatio="none" aria-hidden="true">
    <path d="M258 0 Q300 200 520 210 L520 298 L520 0 Z" fill="var(--arc-gray)"/>
    <path d="M272 0 Q310 188 520 196 L520 0 Z" fill="var(--card-white)"/>
  </svg>

  <div class="wordmark">
    <span class="wordmark__dot"></span>
    <span class="wordmark__name">The Marville<br>Group</span>
  </div>

  <div class="identity">
    <h1 class="identity__name">Daniel Reyes</h1>
    <p class="identity__title">Director of Sales &amp; Marketing</p>
  </div>

  <ul class="contacts">
    <li>
      <svg viewBox="0 0 20 20" aria-hidden="true"><circle cx="10" cy="10" r="9" fill="none" stroke="#fff" stroke-width="1.4"/><path d="M6.5 6.5c0 4 3 7 7 7l1-1.6-2-1.2-1 .8c-1.2-.6-2.1-1.5-2.7-2.7l.8-1-1.2-2z" fill="#fff"/></svg>
      <span>555-418-7093</span>
    </li>
    <li>
      <svg viewBox="0 0 20 20" aria-hidden="true"><circle cx="10" cy="10" r="9" fill="none" stroke="#fff" stroke-width="1.4"/><circle cx="10" cy="10" r="4.5" fill="none" stroke="#fff" stroke-width="1.2"/><path d="M5.5 10h9M10 5.5c-2 3-2 6 0 9M10 5.5c2 3 2 6 0 9" fill="none" stroke="#fff" stroke-width="1"/></svg>
      <span>www.themarvillegroup.example</span>
    </li>
    <li>
      <svg viewBox="0 0 20 20" aria-hidden="true"><circle cx="10" cy="10" r="9" fill="none" stroke="#fff" stroke-width="1.4"/><rect x="5.5" y="7" width="9" height="6.5" fill="#fff"/><path d="M5.5 7l4.5 3.5L14.5 7" fill="none" stroke="#1f5f8c" stroke-width="1"/></svg>
      <span>info@themarvillegroup.example</span>
    </li>
  </ul>
</section>

</body>
</html>
```